Health software company called BRIGHT MERIDIAN, committed to innovation and technological excellence

The powerpoint presentation template is necessary, very necessary is elegant and modern with innovative images and the color palette attached. The presentation will be used for the business plan and investor presentations that we will use to raise funds. Please, recommend a modern typeface, as well as format to be able to use it and incorporate it as part of the company's brand guidelines. Great diversity of technological solutions
Updates

Very low attendance of designers for a high budget. Very few proposals and no capture my interest

Need extra days to review

Need extra days to review

Need extra days to review

Target Market(s)

managers, managers of public and private health centers, government states, investors

Industry/Entity Type

It Company

Font styles to use
Serif

Requirements
Must have
• The powerpoint presentation template is necessary, very necessary is elegant, minimalist and modern with innovative images and the color palette attached. it must be refined in demarcated style
Nice to have
• very nice, visually harmonic avoid saturation
Should not have
• NO dark colors NO dark colors NO dark colors NO dark colors NO dark colors

```html
<!DOCTYPE html>
<html lang="en">
<head>
<meta charset="utf-8">
<title>Bright Meridian – Presentation Template</title>
<link href="https://fonts.googleapis.com/css2?family=Source+Serif+4:opsz,wght@8..60,300;8..60,400;8..60,600&display=swap" rel="stylesheet">
<style>
:root{
  --stage:#a9bccb;
  --blue-deep:#3a86c8;
  --blue-mid:#5a9fd8;
  --blue-bright:#86c0ea;
  --blue-text:#2f7cc0;
  --cyan:#4fb1e6;
  --ink:#3a3f45;
  --ink-soft:#6a7077;
  --paper:#ffffff;
  --paper-soft:#f4f8fb;
  --grey-card:#c3cad0;
  --placeholder:#d2dce4;
  --tl-grey:#b3bec6;
}
*{box-sizing:border-box;margin:0;padding:0}
html,body{width:1200px;height:809px;overflow:hidden}
body{background:var(--stage);font-family:"Source Serif 4",Georgia,serif;font-weight:400;color:var(--ink);position:relative}
.slide{position:absolute;width:358px;height:225px;overflow:hidden;background:var(--paper);box-shadow:0 3px 8px rgba(30,50,70,.22)}
.c1{left:52px}.c2{left:422px}.c3{left:789px}
.r1{top:56px}.r2{top:290px}.r3{top:526px}
.blue-bg{background:radial-gradient(ellipse at 70% 35%,var(--blue-bright) 0%,var(--blue-mid) 45%,var(--blue-deep) 100%);color:#fff}
.abs{position:absolute}
.center{left:0;right:0;text-align:center}
.brand{font-weight:600;letter-spacing:.6px}
.rule{position:absolute;height:1px;background:#dff1fc}

/* cover */
.cover-brand{top:97px;font-size:15px}
.cover-tag{top:123px;font-size:6.3px;letter-spacing:1px;font-weight:300}

/* welcome */
.welcome-title{top:94px;font-size:8.5px}
.welcome-text{top:114px;font-size:6px;line-height:8px;color:#eef7fd;font-weight:300}

/* title slide */
.title-brand{top:16px;right:17px;font-size:9.5px}
.title-main{top:86px;left:39px;font-size:14.5px;font-weight:300;letter-spacing:.2px;white-space:nowrap}
.title-desc{top:106px;left:39px;font-size:8.5px;font-weight:300}
.title-meta{top:150px;left:39px;border-left:1px solid #fff;padding-left:5px;font-size:6.5px;line-height:10px;font-weight:300}

/* section title */
.section-top{position:absolute;left:0;top:0;width:358px;height:168px}
.section-title{top:71px;font-size:15px;font-weight:300}
.section-desc{top:93px;font-size:8.5px;font-weight:300}
.section-brand{top:189px;font-size:9.5px;color:var(--cyan)}
.section-url{top:203px;font-size:6px;color:var(--blue-text)}

/* contents */
.toc-band{position:absolute;left:0;top:0;width:358px;height:42px}
.toc-title{top:24px;left:26px;font-size:11px;color:#fff;font-weight:300}
.toc-item{position:absolute;width:150px}
.toc-item svg{position:absolute;left:0;top:0}
.toc-item h4{position:absolute;left:22px;top:0;font-size:6.5px;font-weight:400;color:var(--blue-text);white-space:nowrap}
.toc-item p{position:absolute;left:22px;top:8px;font-size:4.6px;line-height:5.5px;color:var(--ink);width:135px;font-weight:300}

/* headings */
.slide-heading{top:13px;font-size:11px;color:var(--ink);font-weight:400}
.slide-heading::after{content:"";display:block;width:24px;height:1px;background:var(--cyan);margin:3px auto 0}

/* company */
.company-box{left:22px;top:40px;width:316px;height:86px;background:linear-gradient(100deg,var(--blue-deep),var(--blue-bright))}
.company-brand{left:29px;top:28px;font-size:10px;color:#fff}
.company-note{left:29px;top:44px;font-size:4.6px;line-height:5.5px;color:#eef7fd;font-weight:300}
.company-lead{left:22px;top:133px;width:316px;font-size:5.8px;line-height:7.8px;color:var(--blue-text)}
.company-col{top:172px;font-size:5.4px;line-height:7px;color:var(--ink-soft);font-weight:300}
.company-col b{color:var(--blue-text);font-weight:600;position:absolute;left:0}
.company-col span{position:absolute;left:34px;width:110px}
.company-foot{left:16px;top:213px;font-size:4.6px;color:var(--ink)}
.page-no{right:12px;top:213px;font-size:4.6px;color:var(--ink-soft)}

/* footer band */
.footer{position:absolute;left:0;bottom:0;width:358px;height:19px;background:linear-gradient(90deg,var(--blue-deep),var(--blue-mid));font-size:5.5px;color:#fff;font-weight:300}
.footer .f-brand{position:absolute;left:13px;top:6px;color:#e2f3fd}
.footer .f-title{position:absolute;left:70px;top:6px;border-left:1px solid #cfeafa;padding-left:5px}
.footer .f-url{position:absolute;right:22px;top:6px}
.footer .f-no{position:absolute;right:7px;top:6px;border-left:1px solid #cfeafa;padding-left:4px}

/* images and text */
.photo{position:absolute;top:38px;height:88px;width:145px}
.photo-a{left:29px;background:linear-gradient(180deg,#a9c5dc 0%,#d8cdb8 55%,#8a949c 100%)}
.photo-b{left:184px;background:linear-gradient(135deg,#7d8894 0%,#e3c7b6 50%,#f3efea 100%)}
.caption{position:absolute;top:131px;width:145px}
.caption h4{font-size:7.5px;font-weight:400;color:var(--blue-text)}
.caption p{font-size:5.2px;line-height:6.8px;margin-top:2px;color:var(--ink);font-weight:300}

/* history */
.history{background:var(--paper-soft)}
.ph{position:absolute;top:44px;width:71px;height:48px;background:var(--placeholder);color:#eef3f7;font-size:4.2px;text-align:center;padding-top:14px;line-height:5.5px}
.vline{position:absolute;top:44px;width:1px;height:131px;background:#dbe3e9}
.tl-event{position:absolute;top:135px;width:72px}
.tl-event h5{font-size:5.2px;font-weight:400;color:var(--ink)}
.tl-event p{font-size:4.2px;line-height:5.4px;color:var(--ink-soft);margin-top:3px;font-weight:300}

/* products */
.card{position:absolute;top:34px;width:77px;height:156px}
.card.blue{background:#8cc5ea}.card.grey{background:var(--grey-card)}
.card-photo{position:absolute;left:0;top:0;width:77px;height:72px}
.card-icon{position:absolute;left:30px;top:64px}
.card h5{position:absolute;top:88px;left:0;width:77px;text-align:center;font-size:5.2px;font-weight:600;color:#254560}
.card ul{position:absolute;top:100px;left:6px;width:68px;font-size:4.2px;line-height:5.5px;color:#fff;padding-left:5px}
.card li{margin-bottom:4px}
</style>
</head>
<body>

<!-- Row 1 -->
<section class="slide c1 r1 blue-bg">
  <div class="abs center brand cover-brand">BRIGHT MERIDIAN</div>
  <div class="abs center cover-tag">BRAND STATEMENT GOES HERE</div>
</section>

<section class="slide c2 r1 blue-bg">
  <div class="abs center welcome-title">welcome to BRIGHT MERIDIAN</div>
  <div class="abs center welcome-text">Consectetur adipiscing elit, sed do<br>eiusmod incididunt ut labore et dolore magna aliqua.</div>
  <div class="rule" style="left:171px;top:139px;width:16px"></div>
</section>

<section class="slide c3 r1 blue-bg">
  <div class="abs brand title-brand">BRIGHT MERIDIAN</div>
  <div class="abs title-main">BUSINESS PRESENTATION TITLE</div>
  <div class="abs title-desc">Description Line Here</div>
  <div class="abs title-meta">Dec 29<sup style="font-size:4px">th</sup>,2017<br>Author's Name<br>www.brightmeridian.com</div>
</section>

<!-- Row 2 -->
<section class="slide c1 r2">
  <div class="section-top blue-bg"></div>
  <div class="abs center section-title" style="color:#fff">Business Presentation Title</div>
  <div class="abs center section-desc" style="color:#fff">Description Line Here</div>
  <div class="rule" style="left:167px;top:108px;width:24px;background:#fff"></div>
  <div class="abs center brand section-brand">BRIGHT MERIDIAN</div>
  <div class="abs center section-url">www.brightmeridian.com</div>
</section>

<section class="slide c2 r2">
  <div class="toc-band blue-bg"></div>
  <div class="abs toc-title">table of content</div>
  <svg width="0" height="0" style="position:absolute">
    <defs><symbol id="hex" viewBox="0 0 14 14"><polygon points="7,1 12.5,4 12.5,10 7,13 1.5,10 1.5,4" fill="none" stroke="#2f7cc0" stroke-width=".8"/></symbol></defs>
  </svg>

  <div class="toc-item" style="left:27px;top:65px"><svg width="14" height="14"><use href="#hex"/><text x="7" y="9.3" font-size="5.5" text-anchor="middle" fill="#2f7cc0" font-family="Source Serif 4,serif">1</text></svg><h4>The Company</h4><p>History, the philosophy, mission and vision</p></div>
  <div class="toc-item" style="left:27px;top:85px"><svg width="14" height="14"><use href="#hex"/><text x="7" y="9.3" font-size="5.5" text-anchor="middle" fill="#2f7cc0" font-family="Source Serif 4,serif">2</text></svg><h4>Our Products and Services</h4><p>Reprehenderit in voluptate velit esse cillum<br>dolore eu fugiat nulla pariatur.</p></div>
  <div class="toc-item" style="left:27px;top:112px"><svg width="14" height="14"><use href="#hex"/><text x="7" y="9.3" font-size="5.5" text-anchor="middle" fill="#2f7cc0" font-family="Source Serif 4,serif">3</text></svg><h4>Our Archievement</h4><p>Reprehenderit in voluptate velit esse cillum<br>dolore eu fugiat nulla pariatur.</p></div>
  <div class="toc-item" style="left:27px;top:139px"><svg width="14" height="14"><use href="#hex"/><text x="7" y="9.3" font-size="5.5" text-anchor="middle" fill="#2f7cc0" font-family="Source Serif 4,serif">4</text></svg><h4>The Team</h4><p>Quis autem voluptate velit esse quam nihil molestiae</p></div>
  <div class="toc-item" style="left:27px;top:160px"><svg width="14" height="14"><use href="#hex"/><text x="7" y="9.3" font-size="5.5" text-anchor="middle" fill="#2f7cc0" font-family="Source Serif 4,serif">5</text></svg><h4>Our Awesome Partners</h4><p>Temporibus autem quibusdam et aut officiis<br>debitis aut rerum necessitatibus</p></div>

  <div class="toc-item" style="left:187px;top:65px"><svg width="14" height="14"><use href="#hex"/><text x="7" y="9.3" font-size="5.5" text-anchor="middle" fill="#2f7cc0" font-family="Source Serif 4,serif">6</text></svg><h4>Clients Data and Profit</h4><p>Reprehenderit in voluptate velit esse cillum</p></div>
  <div class="toc-item" style="left:187px;top:85px"><svg width="14" height="14"><use href="#hex"/><text x="7" y="9.3" font-size="5.5" text-anchor="middle" fill="#2f7cc0" font-family="Source Serif 4,serif">7</text></svg><h4>Our Customers Say</h4><p>Quis autem voluptate velit esse quam nihilstia<br>dolore eu fugiat nulla pariatur.</p></div>
  <div class="toc-item" style="left:187px;top:112px"><svg width="14" height="14"><use href="#hex"/><text x="7" y="9.3" font-size="5.5" text-anchor="middle" fill="#2f7cc0" font-family="Source Serif 4,serif">8</text></svg><h4>Our Sales</h4><p>Reprehenderit in voluptate velit esse cillum<br>dolore eu fugiat nulla pariatur.</p></div>
  <div class="toc-item" style="left:187px;top:139px"><svg width="14" height="14"><use href="#hex"/><text x="7" y="9.3" font-size="5.5" text-anchor="middle" fill="#2f7cc0" font-family="Source Serif 4,serif">9</text></svg><h4>Our Data</h4><p>Quis autem voluptate velit esse quam nihil molestiae</p></div>
  <div class="toc-item" style="left:187px;top:160px"><svg width="14" height="14"><use href="#hex"/><text x="7" y="9.3" font-size="5" text-anchor="middle" fill="#2f7cc0" font-family="Source Serif 4,serif">10</text></svg><h4>Contact Us</h4><p>Temporibus autem quibusdam et aut officiis<br>debitis aut rerum necessitatibus</p></div>
</section>

<section class="slide c3 r2">
  <div class="abs center slide-heading">The Company</div>
  <div class="abs company-box" role="img" aria-label="Photo of a modern glass office building in light blue tones">
    <div class="abs brand company-brand">BRIGHT MERIDIAN</div>
    <div class="abs company-note">Your company commitment statement<br>can be placed here with image representative.</div>
  </div>
  <div class="abs company-lead">Consectetur adipiscing elit, sed do eiusmod incididunt ut labore et dolore magna aliqua. Consectetur adipiscing elit, sed do eiusmod incididunt ut labore et dolore magna aliqua. Consectetur adipiscing elit, sed do eiusmod incididunt ut labore et dolore magna aliqua.</div>
  <div class="abs company-col" style="left:22px;width:150px"><b>our vision</b><span>Consectetur adipiscing elit, sed do eiusmod incididunt ut labore et dolore magna aliqua.</span></div>
  <div class="abs company-col" style="left:187px;width:150px"><b>our mission</b><span>Consectetur adipiscing elit, sed do eiusmod incididunt ut labore et dolore magna aliqua.</span></div>
  <div class="abs company-foot">Presentation Title goes here &nbsp;|&nbsp; www.brightmeridian.com</div>
  <div class="abs page-no">02</div>
</section>

<!-- Row 3 -->
<section class="slide c1 r3">
  <div class="abs center slide-heading">Images and Text</div>
  <div class="photo photo-a" role="img" aria-label="Photo of a businessman on a rooftop looking over a city skyline"></div>
  <div class="photo photo-b" role="img" aria-label="Photo of a team stacking hands together"></div>
  <div class="caption" style="left:28px"><h4>Lorem Ipsum</h4><p>Lorem ipsum dolor sit amet, consectetur adipiscing elit, sed do eiusmod tempor incididunt ut labore et dolore magna aliqua. Ut enim ad minim veniam, quis nostrud exercitation ullamco laboris nisi ut aliquip ex ea</p></div>
  <div class="caption" style="left:184px"><h4>Lorem Ipsum</h4><p>Lorem ipsum dolor sit amet, consectetur adipiscing elit, sed do eiusmod tempor incididunt ut labore et dolore magna aliqua. Ut enim ad minim veniam, quis nostrud exercitation ullamco laboris nisi ut aliquip ex ea</p></div>
  <footer class="footer"><span class="f-brand brand">BRIGHT MERIDIAN</span><span class="f-title">Business Presentation Title</span><span class="f-url">www.brightmeridian.com</span><span class="f-no">01</span></footer>
</section>

<section class="slide c2 r3 history">
  <div class="abs center slide-heading">Our History</div>
  <div class="vline" style="left:22px"></div><div class="vline" style="left:103px"></div><div class="vline" style="left:184px"></div><div class="vline" style="left:265px"></div>
  <div class="ph" style="left:28px">IMAGE<br>PLACE HOLDER<br>5 X 3.5 CM</div>
  <div class="ph" style="left:109px">IMAGE<br>PLACE HOLDER<br>5 X 3.5 CM</div>
  <div class="ph" style="left:190px">IMAGE<br>PLACE HOLDER<br>5 X 3.5 CM</div>
  <div class="ph" style="left:270px">IMAGE<br>PLACE HOLDER<br>5 X 3.5 CM</div>
  <svg class="abs" style="left:0;top:116px" width="358" height="14" viewBox="0 0 358 14">
    <rect x="0" y="0" width="358" height="10" fill="#a8d6f1"/>
    <polygon points="0,0 66,0 71,5 66,10 0,10" fill="#9aa7b1"/>
    <polygon points="66,0 147,0 152,5 147,10 66,10 71,5" fill="var(--tl-grey)"/>
    <polygon points="147,0 228,0 233,5 228,10 147,10 152,5" fill="#c8d1d8"/>
    <polygon points="228,0 314,0 319,5 314,10 228,10 233,5" fill="var(--blue-deep)"/>
    <polygon points="20,10 25,10 22.5,13" fill="#9aa7b1"/>
    <polygon points="101,10 106,10 103.5,13" fill="var(--tl-grey)"/>
    <polygon points="182,10 187,10 184.5,13" fill="#c8d1d8"/>
    <polygon points="263,10 268,10 265.5,13" fill="var(--blue-deep)"/>
    <g font-family="Source Serif 4,serif" font-size="5.2" fill="#fff" font-weight="600">
      <text x="16" y="7">2012</text><text x="97" y="7">2013</text><text x="178" y="7">2014</text><text x="259" y="7">2017</text>
    </g>
  </svg>
  <div class="tl-event" style="left:27px"><h5>22 Dec,2012</h5><p>Lorem ipsum dolor sit amet, consectetur adipiscing elit, sed do eiusmod tempor incididunt ut labore et dolore magna aliqua.</p></div>
  <div class="tl-event" style="left:108px"><h5>12 Feb,2013</h5><p>Lorem ipsum dolor sit amet, consectetur adipiscing elit, sed do eiusmod tempor incididunt ut labore et dolore magna aliqua.</p></div>
  <div class="tl-event" style="left:189px"><h5>15 Mar,2014</h5><p>Lorem ipsum dolor sit amet, consectetur adipiscing elit, sed do eiusmod tempor incididunt ut labore et dolore magna aliqua.</p></div>
  <div class="tl-event" style="left:270px"><h5>2 April,2017</h5><p>Lorem ipsum dolor sit amet, consectetur adipiscing elit, sed do eiusmod tempor incididunt ut labore et dolore magna aliqua.</p></div>
  <footer class="footer" style="background:linear-gradient(90deg,#e1eaf1,#c8d8e4);color:var(--ink)"><span class="f-brand brand" style="color:var(--blue-text)">BRIGHT MERIDIAN</span><span class="f-title" style="border-color:#9fb3c2">Business Presentation Title</span><span class="f-url">www.brightmeridian.com</span><span class="f-no" style="border-color:#9fb3c2">01</span></footer>
</section>

<section class="slide c3 r3">
  <div class="abs center slide-heading">Our Product and Services</div>
  <svg width="0" height="0" style="position:absolute"><defs>
    <symbol id="badge" viewBox="0 0 17 18"><polygon points="8.5,0.5 16,4.5 16,13.5 8.5,17.5 1,13.5 1,4.5"/></symbol>
  </defs></svg>

  <div class="card blue" style="left:19px">
    <div class="card-photo" role="img" aria-label="Photo of hands working with documents and a laptop" style="background:linear-gradient(160deg,#e6ecf1,#a9b9c7)"></div>
    <svg class="card-icon" width="17" height="18"><use href="#badge" fill="#3a86c8"/><rect x="5" y="6" width="7" height="5" fill="none" stroke="#fff" stroke-width=".8"/><line x1="6.5" y1="12.5" x2="10.5" y2="12.5" stroke="#fff" stroke-width=".8"/></svg>
    <h5>LOREM IPSUM</h5>
    <ul><li>Lorem ipsum dolor sit amet, consectetur adipiscing elit, sed do eiusmod tempor incididunt ut labore et dolore magna aliqua.</li><li>Consectetur adipiscing elit, sed do eiusmod</li></ul>
  </div>
  <div class="card grey" style="left:100px">
    <div class="card-photo" role="img" aria-label="Photo of a person typing on a laptop" style="background:linear-gradient(160deg,#9a9da1,#d7d2cd)"></div>
    <svg class="card-icon" width="17" height="18"><use href="#badge" fill="#98a2aa"/><rect x="5.5" y="5.5" width="6" height="6" fill="none" stroke="#fff" stroke-width=".8"/><circle cx="8.5" cy="8.5" r="1.3" fill="#fff"/></svg>
    <h5>LOREM IPSUM</h5>
    <ul><li>Lorem ipsum dolor sit amet, consectetur adipiscing elit, sed do eiusmod tempor incididunt ut labore et dolore magna aliqua.</li><li>Consectetur adipiscing elit, sed do eiusmod</li></ul>
  </div>
  <div class="card blue" style="left:181px">
    <div class="card-photo" role="img" aria-label="Photo of a hand touching a glowing digital network" style="background:linear-gradient(160deg,#3f7fbf,#8cc3ec)"></div>
    <svg class="card-icon" width="17" height="18"><use href="#badge" fill="#3a86c8"/><circle cx="8.5" cy="9" r="3.6" fill="none" stroke="#fff" stroke-width=".8"/><line x1="4.9" y1="9" x2="12.1" y2="9" stroke="#fff" stroke-width=".6"/><ellipse cx="8.5" cy="9" rx="1.5" ry="3.6" fill="none" stroke="#fff" stroke-width=".6"/></svg>
    <h5>LOREM IPSUM</h5>
    <ul><li>Lorem ipsum dolor sit amet, consectetur adipiscing elit, sed do eiusmod tempor incididunt ut labore et dolore magna aliqua.</li><li>Consectetur adipiscing elit, sed do eiusmod</li></ul>
  </div>
  <div class="card grey" style="left:262px">
    <div class="card-photo" role="img" aria-label="Photo of a tablet and payment card on a bright desk" style="background:linear-gradient(160deg,#f3f0ea,#d6bf9c)"></div>
    <svg class="card-icon" width="17" height="18"><use href="#badge" fill="#98a2aa"/><path d="M5 11 h7 a2 2 0 0 0 -1 -3.8 a2.6 2.6 0 0 0 -5 .6 a1.7 1.7 0 0 0 -1 3.2z" fill="none" stroke="#fff" stroke-width=".8"/></svg>
    <h5>LOREM IPSUM</h5>
    <ul><li>Lorem ipsum dolor sit amet, consectetur adipiscing elit, sed do eiusmod tempor incididunt ut labore et dolore magna aliqua.</li><li>Consectetur adipiscing elit, sed do eiusmod</li></ul>
  </div>
  <footer class="footer"><span class="f-brand brand">BRIGHT MERIDIAN</span><span class="f-title">Business Presentation Title</span><span class="f-url">www.brightmeridian.com</span><span class="f-no">01</span></footer>
</section>

</body>
</html>
```